Flyer-Design für Wechseljahresberatung
Zielgruppe
Zielgruppe: überwiegend Frauen
psycholog. Beratung in allen Lebenslagen, Wechseljahresberatung , Gesundheits- und Ernährungsberatung, Fastenbegleitung, Trauerbegleitung, Bachblütenberatung,Klangmassagen
Aufgabenstellung
es geht um einen 6teiligen Kurs für Frauen zwischen Ende 30 bis Ende 60. Beginn der Wechseljahre , Leben in den Wechseljahren und was kommt danach? Wie erkennt man (Frau) körperl. oder seelische Probleme, die schon auf We.jahre hindeuten? Wie gehe Frau damit um? Was passiert in den We.jahren? Was kann Frau selbst tun, um die We.jahre so gut wie möglich zu erleben? Im Kurs werden natürliche Hilfsmittel besprochen und erklärt, Entspannungstechniken vermittelt , die Psyche gestärkt, sodaß die betroffenen Frauen bei auftretenden We.jahrsproblemen die Möglichkeit haben,sich selbst helfen zu können.

```html
<!DOCTYPE html>
<html lang="de">
<head>
<meta charset="utf-8">
<title>Wechseljahres Beratung – Informationsbroschüre</title>
<link rel="stylesheet" href="https://fonts.googleapis.com/css2?family=Alfa+Slab+One&family=Arvo:ital,wght@1,700&family=Kalam:wght@400&family=Tinos:wght@400&display=swap">
<style>
  :root {
    --teal: #6bbab9;
    --teal-dark: #3e6468;
    --pink: #d8305f;
    --panel: #e9e9e9;
    --card: #ffffff;
    --quote: #c9d2d6;
    --bg: #f4f4f4;
  }
  * { margin: 0; padding: 0; box-sizing: border-box; }
  html, body { width: 1149px; height: 1200px; overflow: hidden; background: var(--bg); }
  .flyer { position: relative; width: 1149px; height: 1200px; }
  .page {
    position: absolute; top: 40px; width: 525px; height: 1115px;
    background: var(--panel);
  }
  .page--back { left: 50px; }
  .page--front { left: 578px; }
  .card {
    position: absolute; background: var(--card); border-radius: 30px; overflow: hidden;
    top: 33px; width: 461px; height: 1047px;
  }
  .page--back .card { left: 34px; }
  .page--front .card { left: 34px; }
  .card__band {
    position: absolute; left: 0; right: 0; bottom: 0; height: 278px; background: var(--teal);
  }
  .quote {
    position: absolute; left: 0; right: 0; top: 343px; text-align: center;
    font-family: "Arvo", Georgia, serif; font-style: italic; font-weight: 700;
    font-size: 27px; line-height: 28px; color: var(--quote);
  }
  .contact {
    position: absolute; left: 27px; top: 30px; color: #fff;
    font-family: "Tinos", "Times New Roman", serif; font-size: 17px; line-height: 23px;
  }
  .contact p + p { margin-top: 23px; }
  .photo { position: absolute; left: 635px; top: 40px; width: 494px; height: 494px; }
  .badge { position: absolute; left: 640px; top: 397px; width: 162px; height: 162px; }
  .badge__text {
    position: absolute; left: 640px; top: 436px; width: 162px; text-align: center;
    font-family: "Kalam", cursive; font-size: 27px; line-height: 36px; color: #fff;
    transform: rotate(-6deg);
  }
  .title { position: absolute; left: 612px; width: 461px; text-align: center; font-family: "Alfa Slab One", Georgia, serif; }
  .title--top { top: 606px; font-size: 40px; letter-spacing: 1px; color: var(--teal-dark); }
  .title--main {
    top: 645px; left: 596px; width: 493px; font-size: 76px; letter-spacing: 2px; color: var(--pink);
  }
  .subtitle {
    position: absolute; left: 612px; width: 461px; top: 724px; text-align: center;
    font-family: "Kalam", cursive; font-size: 22px; color: var(--teal); transform: rotate(-3deg);
  }
  .label {
    position: absolute; left: 612px; width: 461px; top: 800px; text-align: center;
    font-family: "Tinos", "Times New Roman", serif; font-size: 24px; color: var(--teal-dark);
  }
  .intro {
    position: absolute; left: 0; right: 0; top: 52px; text-align: center; padding: 0 30px;
    font-family: "Tinos", "Times New Roman", serif; font-size: 25px; line-height: 33px; color: #fff;
  }
</style>
</head>
<body>
<main class="flyer">
  <section class="page page--back">
    <div class="card">
      <p class="quote">Alles hat<br>nur die<br>Bedeutung,<br>die man<br>ihm gibt.</p>
      <div class="card__band">
        <div class="contact">
          <p>Kontakt:</p>
          <p>Lumara<br>Helga Morsbach-Tiel<br>Lindenweg 12<br>6400XY Beekhoven / NL</p>
          <p>Telefon: 0241/00 00 12 34<br>oder&nbsp; +31 (0) 45/5 00 0 00<br>Mail: mondhalmkreise.praxis@beispielpost.de</p>
        </div>
      </div>
    </div>
  </section>

  <section class="page page--front">
    <div class="card">
      <div class="card__band">
        <p class="intro">InformationsbroschüreMa-<br>iorro in reius, quianis quosto dolectem aces alicaborum rem rerae sus de corepellesto omniend emollut landae</p>
      </div>
    </div>
  </section>

  <svg class="photo" viewBox="0 0 494 494" role="img" aria-label="Foto: zwei lächelnde Frauen, Mutter und Tochter, Wange an Wange">
    <defs>
      <linearGradient id="photoTone" x1="0" y1="0" x2="1" y2="1">
        <stop offset="0" stop-color="#e9e1d8"/>
        <stop offset="0.5" stop-color="#d9b7a6"/>
        <stop offset="1" stop-color="#e8c6cf"/>
      </linearGradient>
    </defs>
    <circle cx="247" cy="247" r="240" fill="#fff"/>
    <circle cx="247" cy="247" r="228" fill="url(#photoTone)"/>
  </svg>

  <svg class="badge" viewBox="0 0 162 162" aria-hidden="true">
    <circle cx="81" cy="81" r="80" fill="#fff"/>
    <circle cx="81" cy="81" r="71" fill="var(--teal)"/>
  </svg>
  <p class="badge__text">für Sie ab<br>30 Jahre</p>

  <h1 class="title title--top">WECHSELJAHRES</h1>
  <h2 class="title title--main">BERATUNG</h2>
  <p class="subtitle">6 Teiliger Kurs</p>
  <p class="label">Informationsbroschüre</p>
</main>
</body>
</html>
```